Website Design for new skincare product launch/rebranding

The Dew Harbor website is currently live and built through Pagelume.com. While the existing site has served as a strong starting point, I’m now looking to elevate the overall experience with a complete redesign that reflects the growth and vision of the brand. This will be a full visual and functional revamp — not just a refresh — with the goal of creating a more elevated, intuitive, and conversion-focused platform. I’m looking for a designer who can not only reimagine the layout and visuals, but also collaborate on optimizing the user journey and site structure for both storytelling and sales.

Target Market(s)

Age 25- 45 (core), with secondary appeal to 18-55. Primarily women, but gender inclusive. Wellness/Holistic Beauty/Organic Ingredients, Botanical.

Industry/Entity Type

Beauty, aesthetics, wellness.

Number of Pages Required

5+ page

Font styles to use
Other font styles liked:
• Thorvale Sans Family

Colors

Designer to choose colors to be used in the design.

Requirements
Must have
• Include standard pages (Home, Our Story/Values, Shop, Product Detail with ingredients/description/etc., Contact) and any other recommended sections to optimize conversion. Minimal, clean, calming visual. Seamlessly integrate with Vendara for all product sales.
Nice to have
• Company colors are attached in images, along with first two products that are launching. One called Lumivelt, and one called Serapoise. Fonts and shapes need to align accordingly. Feel elevated, neutral, and luxe while maintaining a grounded, earthy minimalism. Visual inspiration includes brands like Maple Tenet, Vessa Orlaine, and TOrveli — minimal yet high-end, with thoughtful use of whitespace, typography, and subtle movement. Would LOVE to have movement (short clip GIF) on either the home page or ingredient page, reference TOrveli website (homepage or LumaKnit Process™ Tab)
Should not have
• dark colors, complex design elements, too many different fonts. For ingredients, stick to botanical images and information only, with no mentions of CBD or use of leaf imagery.

```html
<!DOCTYPE html>
<html lang="en">
<head>
<meta charset="utf-8">
<title>Dew Harbor — Botanical Balance Meets Science</title>
<link rel="stylesheet" href="https://fonts.googleapis.com/css2?family=Marcellus&family=Montserrat:wght@400;500;600;700&display=swap">
<style>
:root{
  --backdrop:#4b4b4b;
  --white:#ffffff;
  --taupe:#a88b78;
  --taupe-deep:#9c7b60;
  --blush:#ebe3df;
  --stone:#9a9b96;
  --card:#f6f6f6;
  --ink:#3c3c3c;
  --heading:#8a8a88;
  --muted:#c9bdb5;
}
*{margin:0;padding:0;box-sizing:border-box}
html,body{width:1200px;height:3119px;overflow:hidden}
body{background:var(--backdrop);font-family:'Montserrat',sans-serif;color:var(--ink)}
.page{position:absolute;left:81px;top:81px;width:1038px;height:2956px;background:var(--white);overflow:hidden;box-shadow:0 6px 30px rgba(0,0,0,.45)}
.abs{position:absolute}
.serif{font-family:'Marcellus',serif;font-weight:400}

/* hero */
.hero{left:0;top:0;width:1038px;height:600px;background:linear-gradient(100deg,#a98b77 0%,#a98c79 45%,#b49884 65%,#c7ae9c 80%,#b08f7c 100%)}
.hero-products{left:755px;top:180px;width:260px;height:330px;background:linear-gradient(90deg,#f1f1f1 0%,#e6e6e6 45%,#b9b9b9 60%,#c9c9c9 100%);border-radius:6px;opacity:.9}
.topline{top:8px;right:12px;font-size:8.5px;color:var(--white);font-weight:600;display:flex;gap:42px}
.topline span{display:flex;align-items:center;gap:5px}
.nav{left:537px;top:25px;width:501px;height:36px;background:var(--stone);display:flex;align-items:center;justify-content:space-around;padding:0 10px}
.nav a{font-family:'Marcellus',serif;font-size:9px;color:var(--white);text-decoration:none;letter-spacing:.5px}
.nav a.nav-contact{border:1px solid var(--white);padding:3px 10px}
.brand{left:46px;top:24px;font-family:'Marcellus',serif;font-size:44px;color:#ece4de;letter-spacing:1px;line-height:1}
.hero-kicker{left:46px;top:178px;font-family:'Marcellus',serif;font-size:24px;color:var(--white);letter-spacing:.5px}
.hero-title{left:46px;top:206px;font-family:'Marcellus',serif;font-size:50px;line-height:52px;color:var(--white);letter-spacing:1.5px}
.hero-copy{left:46px;top:326px;width:420px;font-size:14.5px;line-height:21px;color:var(--white)}
.btn{display:flex;align-items:center;justify-content:center;font-weight:600;letter-spacing:.4px;text-transform:uppercase}
.btn-shop{left:46px;top:404px;width:120px;height:30px;background:#e6dcd5;color:#7c6b62;font-size:13px}
.btn-learn{left:172px;top:404px;width:121px;height:30px;border:1px solid #e6dcd5;color:#f4ece7;font-size:13px}

/* launches */
.section-title{font-family:'Marcellus',serif;font-size:34px;color:var(--heading);letter-spacing:1px;text-align:center;width:100%}
.launch-title{top:612px}
.launch-sub{top:657px;width:100%;text-align:center;font-size:14.5px}
.card{top:701px;width:329px;height:504px;background:var(--card)}
.card-media{left:0;top:0;width:329px;height:299px;background:linear-gradient(180deg,#f7f7f7,#ededed)}
.card-name{top:320px;width:100%;text-align:center;font-family:'Marcellus',serif;font-size:28px;color:#7d7d7b}
.card-copy{top:368px;left:22px;width:285px;text-align:center;font-size:14px;line-height:21px}
.card-btn{top:446px;left:104px;width:121px;height:29px;background:var(--stone);color:#ecebe8;font-size:12.5px}

/* philosophy */
.philo{left:0;top:1280px;width:1038px;height:640px;background:var(--taupe)}
.philo-photo{left:0;top:1280px;width:540px;height:640px;background:linear-gradient(90deg,#c29a82 0%,#d9b59e 40%,#c39b82 75%,#a88467 100%)}
.philo-title{left:518px;top:1337px;width:474px;text-align:center;font-family:'Marcellus',serif;font-size:34px;color:#f3ece6;letter-spacing:1px}
.philo-sub{left:540px;top:1382px;width:430px;text-align:center;font-size:13.5px;line-height:21px;color:#dcc3b1}
.grid{left:518px;top:1441px;width:474px;height:379px;display:grid;grid-template-columns:1fr 1fr;grid-template-rows:1fr 1fr}
.cell{display:flex;flex-direction:column;align-items:center;padding:20px 16px 0;text-align:center;overflow:hidden}
.cell.dark{background:var(--taupe-deep);color:#f3ebe4}
.cell.light{background:var(--blush);color:#7e6a5c}
.cell-icon{width:60px;height:60px;flex:none}
.cell h3{font-family:'Marcellus',serif;font-weight:400;font-size:20px;line-height:24px;margin-top:16px;letter-spacing:.5px}
.cell.light h3{color:#a07a5d}
.cell p{font-size:10.5px;line-height:14.5px;margin-top:8px}

/* story */
.story-photo-a{left:163px;top:1944px;width:173px;height:230px;background:linear-gradient(135deg,#e8e8e8,#cfcfcf 50%,#bdbdbd)}
.story-photo-b{left:336px;top:1944px;width:173px;height:230px;background:linear-gradient(135deg,#c8c3c0,#aaa4a0 50%,#8f8985)}
.story-kicker{left:544px;top:1966px;font-family:'Marcellus',serif;font-size:14px;color:var(--muted);letter-spacing:.5px}
.story-title{left:544px;top:1985px;font-family:'Marcellus',serif;font-size:34px;line-height:40px;color:#7f7f7d;letter-spacing:1px}
.story-copy{left:544px;top:2033px;width:352px;font-size:10px;line-height:16px;letter-spacing:-.05px}
.story-btn{left:544px;top:2128px;width:159px;height:30px;border:1px solid #9a9a98;color:#777;font-size:13px;font-weight:600;text-transform:none}

/* newsletter */
.stay{left:0;top:2230px;width:1038px;height:500px;background:linear-gradient(90deg,#cdbfab 0%,#d5c7b5 45%,#ddd0c0 100%)}
.stay-photo{left:540px;top:2280px;width:498px;height:420px;background:linear-gradient(90deg,#d9ccbc 0%,#e2c5b1 35%,#d7b29b 60%,#d8cbbb 100%)}
.stay-title{left:70px;top:2348px;width:390px;text-align:center;font-family:'Marcellus',serif;font-size:34px;color:var(--white);letter-spacing:1px}
.stay-sub{left:90px;top:2391px;width:350px;text-align:center;font-size:10.5px;line-height:15.5px}
.field{left:70px;width:390px;background:var(--white);border:1px solid #c8c8c8;font-size:10px;color:#9b9b9b;padding:10px 12px}
.field-email{top:2432px;height:33px}
.field-notes{top:2477px;height:104px}
.subscribe{left:70px;top:2596px;width:390px;height:31px;background:var(--stone);color:var(--white);font-size:10px;letter-spacing:1.5px;font-weight:700}

/* footer */
.footer{left:0;top:2700px;width:1038px;height:256px;background:var(--stone)}
.foot-brand{left:134px;top:2808px;font-family:'Marcellus',serif;font-size:30px;color:var(--white);line-height:1}
.foot-tag{left:233px;top:2801px;width:166px;height:77px;background:#d7d7d4;display:flex;align-items:center;justify-content:center;text-align:center;font-size:10px;line-height:12.5px;color:#4d4d4d;padding:0 14px;clip-path:polygon(0 0,88% 0,100% 100%,0 100%)}
.foot-col{top:2806px;color:var(--white)}
.foot-col h4{font-family:'Marcellus',serif;font-weight:400;font-size:13.5px;letter-spacing:.5px;margin-bottom:3px}
.foot-col li{list-style:none;font-size:10.5px;line-height:16px;display:flex;align-items:center;gap:4px}
.foot-col li::before{content:"";width:0;height:0;border-left:4px solid var(--white);border-top:3px solid transparent;border-bottom:3px solid transparent}
.foot-col.contact li::before{display:none}
.dot{width:8px;height:8px;background:var(--white);display:inline-block}
.dot.round{border-radius:50%}
.copyright{left:484px;top:2916px;font-size:10px;color:var(--white)}
</style>
</head>
<body>
<div class="page">

  <!-- hero -->
  <section class="abs hero" role="img" aria-label="Portrait of a woman with glowing skin against a warm taupe backdrop"></section>
  <div class="abs hero-products" role="img" aria-label="Serapoise balm tube and Lumivelt serum dropper bottle"></div>
  <div class="abs topline">
    <span><svg width="10" height="7" viewBox="0 0 10 7"><rect x=".5" y=".5" width="9" height="6" fill="none" stroke="#fff"/><path d="M.5 .5 5 4 9.5 .5" fill="none" stroke="#fff"/></svg>Email: hello@dewharbor.com</span>
    <span><svg width="9" height="9" viewBox="0 0 10 10"><path d="M2 1 4 3 3 4.5Q4.5 6.5 5.5 7L7 6 9 8 8 9.5Q3 9 .5 2Z" fill="#fff"/></svg>Phone: (555) 014-2290</span>
  </div>
  <nav class="abs nav">
    <a href="#">HOME</a><a href="#">ABOUT</a><a href="#">WHY CHOOSE US</a><a href="#">SERVICES</a><a class="nav-contact" href="#">CONTACT</a>
  </nav>
  <div class="abs brand">DEW HARBOR</div>
  <div class="abs hero-kicker">BOTANICAL</div>
  <h1 class="abs hero-title serif">BALANCE MEETS<br>SCIENCE</h1>
  <p class="abs hero-copy">Discover Lumivelt Serum &amp; Serapoise Balm — our newest botanically-infused skincare launches designed to hydrate, nourish and align your skin.</p>
  <a class="abs btn btn-shop">Shop Now</a>
  <a class="abs btn btn-learn">Learn More</a>
  <svg class="abs" style="left:0;top:480px" width="1038" height="130" viewBox="0 0 1038 130">
    <path d="M0 40 C150 20 240 0 330 0 C600 0 760 80 940 80 C990 80 1020 76 1038 72 V130 H0Z" fill="#fff"/>
    <path d="M95 22 C300 -4 560 35 700 60 C820 82 900 84 935 78 C860 96 760 92 640 70 C470 38 300 14 95 22Z" fill="#9a9b96"/>
  </svg>

  <!-- new launches -->
  <h2 class="abs section-title launch-title">NEW LAUNCHES</h2>
  <p class="abs launch-sub">Elevate your routine with our carefully formulated botanical essentials.</p>

  <article class="abs card" style="left:163px">
    <div class="abs card-media" role="img" aria-label="Serapoise Botanical Balm tube"></div>
    <h3 class="abs card-name">Serapoise Balm</h3>
    <p class="abs card-copy">A botanical balm that locks in moisture, reduces inflammation, and restores harmony to dry, sensitive skin.</p>
    <a class="abs btn card-btn">Shop Balm</a>
  </article>
  <article class="abs card" style="left:544px">
    <div class="abs card-media" role="img" aria-label="Lumivelt Botanical Serum dropper bottle"></div>
    <h3 class="abs card-name">Lumivelt Serum</h3>
    <p class="abs card-copy">A weightless, glass-like serum infused with hydrating botanicals and natural humectants for plump, radiant skin.</p>
    <a class="abs btn card-btn">Shop Balm</a>
  </article>
  <svg class="abs" style="left:490px;top:700px" width="60" height="510" viewBox="0 0 60 510">
    <path d="M37 0 C70 150 -10 300 10 508 C0 300 58 160 37 0Z" fill="#9a9b96"/>
  </svg>

  <!-- philosophy -->
  <section class="abs philo"></section>
  <div class="abs philo-photo" role="img" aria-label="Woman applying serum with a glass dropper"></div>
  <svg class="abs" style="left:0;top:1250px" width="1038" height="110" viewBox="0 0 1038 110">
    <path d="M0 0 H1038 V48 C900 28 760 20 620 28 C420 40 260 70 0 56Z" fill="#fff"/>
    <path d="M95 72 C300 58 520 26 720 10 C850 0 920 8 935 16 C860 10 760 16 640 32 C470 54 300 74 95 72Z" fill="#9a9b96"/>
  </svg>
  <h2 class="abs philo-title">OUR PHILOSOPHY</h2>
  <p class="abs philo-sub">Rooted in botanicals, guided by science. Every formula honors your skin and the planet.</p>
  <div class="abs grid">
    <div class="cell dark">
      <svg class="cell-icon" viewBox="0 0 60 60"><circle cx="30" cy="30" r="28" fill="none" stroke="#f3ebe4" stroke-width="1.2"/><circle cx="30" cy="24" r="7" fill="none" stroke="#f3ebe4" stroke-width="1.2"/><path d="M16 38 Q30 30 44 38 L40 44 H20Z" fill="none" stroke="#f3ebe4" stroke-width="1.2"/></svg>
      <h3>Sustainable</h3>
      <p>Eco-friendly packaging and low-impact sourcing guide our every decision.</p>
    </div>
    <div class="cell light">
      <svg class="cell-icon" viewBox="0 0 60 60"><circle cx="30" cy="30" r="28" fill="none" stroke="#a07a5d" stroke-width="1.2"/><circle cx="24" cy="26" r="5" fill="none" stroke="#a07a5d" stroke-width="1.2"/><circle cx="36" cy="34" r="5" fill="none" stroke="#a07a5d" stroke-width="1.2"/><path d="M28 29 33 31" stroke="#a07a5d" stroke-width="1.2"/></svg>
      <h3>Botanical Science</h3>
      <p>We pair time-honored botanicals with clinically studied ingredients.</p>
    </div>
    <div class="cell light">
      <svg class="cell-icon" viewBox="0 0 60 60"><circle cx="30" cy="30" r="28" fill="none" stroke="#a07a5d" stroke-width="1.2"/><path d="M30 16 Q36 24 30 34 Q24 24 30 16Z M18 30 Q30 32 30 44 Q30 32 42 30" fill="none" stroke="#a07a5d" stroke-width="1.2"/></svg>
      <h3>Holistic Beauty</h3>
      <p>We treat skin as a whole — mind, body, and spirit — for lasting glow.</p>
    </div>
    <div class="cell dark">
      <svg class="cell-icon" viewBox="0 0 60 60"><circle cx="30" cy="30" r="28" fill="none" stroke="#f3ebe4" stroke-width="1.2"/><rect x="20" y="28" width="20" height="14" fill="none" stroke="#f3ebe4" stroke-width="1.2"/><path d="M24 28 V20 M30 28 V16 M36 28 V21" stroke="#f3ebe4" stroke-width="1.2"/></svg>
      <h3>Clean &amp; Organic</h3>
      <p>A botanical balm that locks in moisture, reduces inflammation, and restores harmony to dry, sensitive skin.</p>
    </div>
  </div>
  <svg class="abs" style="left:0;top:1845px" width="1038" height="90" viewBox="0 0 1038 90">
    <path d="M0 40 C200 20 420 30 600 50 C780 68 920 40 1038 14 V90 H0Z" fill="#fff"/>
    <path d="M95 30 C300 22 520 52 700 68 C820 78 900 74 935 70 C860 82 760 84 640 76 C470 62 300 34 95 30Z" fill="#9a9b96"/>
  </svg>

  <!-- story -->
  <div class="abs story-photo-a" role="img" aria-label="Serum bottle, balm tube and open jar on marble"></div>
  <div class="abs story-photo-b" role="img" aria-label="Hands applying cream, in soft monochrome"></div>
  <div class="abs story-kicker">DEW HARBOR:</div>
  <h2 class="abs story-title">OUR STORY</h2>
  <p class="abs story-copy">Founded with a passion for aligning skin with nature, we create botanically powered skincare that renews, restores and respects your skin's natural harmony. Each product begins with a carefully sourced blend of herbs, flowers and oils, supported by gentle science to deliver visible results without compromise.</p>
  <a class="abs btn story-btn">Explore Our Values</a>

  <!-- newsletter -->
  <section class="abs stay"></section>
  <div class="abs stay-photo" role="img" aria-label="Woman resting her cheek on her hand, fresh glowing skin"></div>
  <svg class="abs" style="left:0;top:2210px" width="1038" height="110" viewBox="0 0 1038 110">
    <path d="M0 0 H1038 V30 C900 30 780 44 640 62 C480 80 300 84 0 76Z" fill="#fff"/>
    <path d="M95 86 C300 84 520 46 720 22 C850 8 920 14 935 16 C860 16 760 26 640 44 C470 70 300 90 95 86Z" fill="#9a9b96"/>
  </svg>
  <h2 class="abs stay-title">STAY ALIGNED</h2>
  <p class="abs stay-sub">Join our newsletter for early access to launches, botanical insights and exclusive offers.</p>
  <div class="abs field field-email">Your email address</div>
  <div class="abs field field-notes">Questions or feedback?</div>
  <a class="abs btn subscribe">Subscribe</a>

  <!-- footer -->
  <svg class="abs" style="left:0;top:2660px" width="1038" height="70" viewBox="0 0 1038 70">
    <path d="M0 50 C180 20 360 10 520 24 C700 40 880 30 1038 6 V70 H0Z" fill="#9a9b96"/>
    <path d="M60 40 C260 28 480 40 660 48 C820 54 940 30 1010 10 C930 46 800 64 640 60 C460 54 260 40 60 40Z" fill="#d9cfc2"/>
  </svg>
  <footer class="abs footer"></footer>
  <div class="abs foot-brand">Dew<br>Harbor</div>
  <div class="abs foot-tag">Botanically balanced skincare, crafted for harmony between nature and science.</div>
  <div class="abs foot-col" style="left:484px">
    <h4>LINKS</h4>
    <ul><li>Home</li><li>Our Story</li><li>Shop</li><li>Values</li></ul>
  </div>
  <div class="abs foot-col" style="left:600px">
    <h4>Support</h4>
    <ul><li>FAQ</li><li>Shipping &amp; Returns</li><li>Privacy Policy</li><li>Terms of Service</li></ul>
  </div>
  <div class="abs foot-col contact" style="left:769px">
    <h4>CONTACT</h4>
    <ul><li><span class="dot"></span>hello@dewharbor.com</li><li><span class="dot round"></span>Glimmer</li><li><span class="dot round"></span>Reelto</li></ul>
  </div>
  <div class="abs copyright">© 2025 Dew Harbor. All rights reserved.</div>

</div>
</body>
</html>
```